Electrical Contracting Business Website

Require website done for my contracting business.
Partly done one but really dont have time.

You can view the current one at http://brelton.net.au

You can use any info/styles/photos from the current website

I like the orange color of the logo so id like things to be with that
Unfortunatly being a new business (Sept 2015) I havent got alot of photos . but if you require any for any of the specifics listed in the doc file ill have a look to see what I have.

I am targeting mainly commercial / industrial clients. Which also includes government and mining.

Target Market(s)

People requiring electricians

Industry/Entity Type

Electrician

Coding

Number of Pages Required

Colors
f37122

Requirements
Must have
• logo with EC Number
• Keep it simple and not to complicated
• Comply with the current html / style sheet standards.
• Desktop/Mobile Version compatability
Nice to have
• additional photos.
• The domestic lifts we install are by vostrel I dont have any photos of them unfortunately.
Should not have
• change colour of logo

```html
<!DOCTYPE html>
<html lang="en">
<head>
<meta charset="utf-8">
<title>Brelton Engineering</title>
<link rel="stylesheet" href="https://fonts.googleapis.com/css2?family=Open+Sans:ital,wght@0,400;0,600;0,700;0,800;1,400&display=swap">
<style>
:root{
  --orange:#f37122;
  --ink:#222;
  --text:#666;
  --muted:#8a8a8a;
  --line:#e3e3e3;
  --dark:#2b2b2b;
  --darker:#232323;
  --white:#fff;
}
*{box-sizing:border-box;margin:0;padding:0}
html,body{width:1200px;height:2456px;overflow:hidden}
body{font-family:"Open Sans",Arial,sans-serif;color:var(--text);background:var(--white);position:relative}
.abs{position:absolute}
ul{list-style:none}

/* header */
.site-header{left:0;top:0;width:1200px;height:106px;background:var(--white);z-index:5}
.brand{left:98px;top:24px;font-size:38px;font-weight:800;color:var(--orange);letter-spacing:-1px;display:flex;align-items:center;gap:10px}
.brand .mark{width:30px;height:30px;border-radius:50%;background:var(--orange)}
.topbar{top:24px;right:98px;display:flex;gap:40px;font-size:13px;color:var(--muted)}
.topbar span{display:flex;align-items:center;gap:8px}
.topbar b{font-weight:400;color:var(--orange)}
.main-nav{top:67px;left:445px;width:657px;display:flex;justify-content:space-between;font-size:13px;letter-spacing:1px;text-transform:uppercase;color:#777}
.dropdown{left:435px;top:101px;width:179px;height:128px;background:var(--white);box-shadow:0 2px 8px rgba(0,0,0,.18);padding:14px 0 0 20px;font-size:11.5px;color:var(--muted);z-index:6}
.dropdown li{height:26px}
.dropdown li::before{content:"›";margin-right:8px}

/* hero */
.hero{left:0;top:106px;width:1200px;height:546px;background:linear-gradient(120deg,#5d4a2c 0%,#7a6a55 35%,#9a7f6c 60%,#4a3d34 100%)}
.hero::after{content:"";position:absolute;inset:0;background:rgba(0,0,0,.35)}
.hero-copy{left:0;top:284px;width:1200px;text-align:center;z-index:2}
.hero-title{font-size:42px;font-weight:800;line-height:54px;color:var(--orange);text-transform:uppercase;letter-spacing:1px}
.hero-tagline{font-size:29px;font-weight:400;line-height:40px;color:var(--white);letter-spacing:2px;margin-top:4px}
.hero-actions{margin-top:28px;display:flex;justify-content:center;gap:20px}
.btn{width:196px;height:45px;background:var(--orange);color:var(--white);font-size:14px;font-weight:600;text-transform:uppercase;display:flex;align-items:center;justify-content:center}
.arrow{top:356px;z-index:2;width:48px;height:48px;border-radius:50%;background:rgba(255,255,255,.18)}

/* intro */
.intro-brand{left:155px;top:748px;font-size:52px;font-weight:800;color:var(--orange);display:flex;align-items:center;gap:12px}
.intro-brand .mark{width:44px;height:44px;border-radius:50%;background:var(--orange)}
.intro-rule{left:452px;top:745px;width:1px;height:93px;background:var(--line)}
.intro-text{left:507px;top:745px;width:520px;font-size:12.5px;line-height:23px}

/* work */
.section-title{left:0;width:1200px;text-align:center;font-size:26px;font-weight:800;color:var(--ink);text-transform:uppercase}
.section-sub{left:0;top:954px;width:1200px;text-align:center;font-size:13px}
.tile{top:1013px;width:327px;height:244px}
.tile-orange{left:100px;background:var(--orange);padding:32px 38px;color:var(--white)}
.tile-orange h3{font-size:15px;font-weight:700;text-transform:uppercase;margin-bottom:12px}
.tile-orange li{font-size:13px;line-height:26px}
.tile-orange li::before{content:"›";margin-right:10px}
.tile-panel{left:437px;background:linear-gradient(135deg,#e9e9e6,#6e6e70 60%,#3b3b3d)}
.tile-motors{left:774px;background:linear-gradient(135deg,#b8a58e,#3a3a3a 50%,#1f1f1f)}

/* services */
.services{left:0;top:1342px;width:1200px;height:377px;background:var(--dark)}
.video{left:0;top:1342px;width:601px;height:341px;background:linear-gradient(135deg,#e6e4de 0%,#bfbcb4 45%,#3a3a3c 60%,#d9d6cf 100%)}
.play{left:258px;top:1490px;width:82px;height:82px;border-radius:50%;background:#e84a47;display:flex;align-items:center;justify-content:center}
.video-bar{left:0;top:1683px;width:601px;height:36px;background:#0c0c0c;color:var(--white);font-size:10px}
.services-title{left:684px;top:1411px;font-size:26px;font-weight:800;color:#9a9a9a;text-transform:uppercase}
.svc-list{top:1472px;font-size:13px;color:#bdbdbd}
.svc-list li{height:28.3px}
.svc-list li::before{content:"›";margin-right:12px}

/* testimonials */
.portrait{left:157px;top:1855px;width:190px;height:190px;border-radius:50%;background:radial-gradient(circle at 50% 40%,#c9b7a7,#6a6058 70%,#2a2a2a)}
.quote{left:450px;top:1892px;width:560px;font-size:12.5px;font-style:italic;line-height:23px;color:#888}
.qmark{font-size:44px;color:#ccc;font-family:Georgia,serif}
.t-name{left:450px;top:1993px;font-size:15px;font-weight:700;color:var(--orange)}
.t-role{left:450px;top:2018px;font-size:11.5px;color:var(--ink)}
.t-nav{left:1010px;top:2018px;display:flex;gap:4px}
.t-nav i{width:12px;height:12px;border-radius:50%;background:#bbb}

/* footer */
.site-footer{left:0;top:2128px;width:1200px;height:265px;background:var(--dark)}
.foot-brand{left:98px;top:2222px;font-size:38px;font-weight:800;color:var(--orange);display:flex;align-items:center;gap:10px}
.foot-brand .mark{width:30px;height:30px;border-radius:50%;background:var(--orange)}
.foot-col{top:2168px;font-size:11.5px;color:#999;line-height:23px}
.foot-col h4{font-size:14px;font-weight:700;color:var(--white);text-transform:uppercase;margin-bottom:18px}
.foot-col .more{color:var(--orange);font-weight:600;margin-top:14px;display:block}
.contact-row{display:flex;align-items:center;gap:10px;margin-top:4px}
.bottom-bar{left:0;top:2393px;width:1200px;height:63px;background:var(--darker)}
.badge{left:98px;top:2404px;width:115px;height:40px;background:#3a3a3a;border-radius:3px}
.copyright{left:237px;top:2417px;font-size:11px;color:#999}
.social{left:771px;top:2417px;display:flex;align-items:center;gap:18px;font-size:11px;color:#999}
.social i{width:12px;height:12px;border-radius:50%;background:var(--orange)}
</style>
</head>
<body>

<header class="abs site-header">
  <div class="abs brand"><span class="mark"></span>BRELTON</div>
  <div class="abs topbar">
    <span><svg width="13" height="13" viewBox="0 0 24 24"><path fill="#f37122" d="M6.6 10.8a15 15 0 0 0 6.6 6.6l2.2-2.2c.3-.3.7-.4 1-.2 1.1.4 2.3.6 3.6.6.6 0 1 .4 1 1V20c0 .6-.4 1-1 1A17 17 0 0 1 3 4c0-.6.4-1 1-1h3.5c.6 0 1 .4 1 1 0 1.3.2 2.5.6 3.6.1.3 0 .7-.2 1z"/></svg>Call Us : <b>( 2480 ) 517 902</b></span>
    <span><svg width="14" height="12" viewBox="0 0 24 18"><rect width="24" height="18" rx="2" fill="#f37122"/><path d="M1 2l11 8 11-8" stroke="#fff" stroke-width="2" fill="none"/></svg>Email Us : <b>info@brelton.net.au</b></span>
  </div>
  <nav class="abs main-nav"><span>About Us ⌄</span><span>Residential</span><span>Commercial</span><span>Industrial</span><span>Contact Us</span></nav>
</header>

<section class="abs hero" role="img" aria-label="Photo of a hand testing a switchboard with a yellow multimeter"></section>
<div class="abs arrow" style="left:50px"></div>
<div class="abs arrow" style="left:1102px"></div>
<div class="abs hero-copy">
  <h1 class="hero-title">Brelton Engineering</h1>
  <p class="hero-tagline">DELIVERING UNBEATABLE ELECTRICAL SERVICES</p>
  <div class="hero-actions"><span class="btn">View History</span><span class="btn">Contact Here!</span></div>
</div>

<ul class="abs dropdown"><li>Our Values</li><li>Safety</li><li>Quality</li><li>Reliability</li></ul>

<div class="abs intro-brand"><span class="mark"></span>BRELTON</div>
<div class="abs intro-rule"></div>
<p class="abs intro-text">Lorem Ipsum is simply dummy text of the printing and typesetting industry. Lorem Ipsum has been the industry's standard dummy text ever since the 1500s, when an unknown printer took a galley of type and scrambled it to make a type specimen book. It has survived not only five centuries, but also the leap into electronic typesetting...</p>

<h2 class="abs section-title" style="top:904px">Our Work</h2>
<p class="abs section-sub">Delivering unbeatable electrical services. Contact us now to find out how we can help you with your next electrical solution.</p>
<div class="abs tile tile-orange">
  <h3>Residential Work Includes:</h3>
  <ul><li>Domestic Lifts</li><li>Bore Pumps</li><li>Fault finding</li></ul>
</div>
<div class="abs tile tile-panel" role="img" aria-label="Photo of circuit breakers in a switchboard"></div>
<div class="abs tile tile-motors" role="img" aria-label="Photo of black electric motors"></div>

<section class="abs services"></section>
<div class="abs video" role="img" aria-label="Video still of an open electrical control cabinet with orange conduit"></div>
<div class="abs play"><svg width="30" height="34" viewBox="0 0 30 34"><path d="M2 1l27 16L2 33z" fill="#fff"/></svg></div>
<div class="abs video-bar">
  <svg class="abs" style="left:12px;top:12px" width="10" height="12"><rect width="3" height="12" fill="#fff"/><rect x="7" width="3" height="12" fill="#fff"/></svg>
  <svg class="abs" style="left:46px;top:11px" width="18" height="14" viewBox="0 0 18 14"><path d="M0 4h4l5-4v14l-5-4H0z" fill="#fff"/><path d="M12 3q3 4 0 8M14 1q5 6 0 12" stroke="#fff" fill="none"/></svg>
  <span class="abs" style="left:78px;top:0;width:1px;height:36px;background:#333"></span>
  <span class="abs" style="left:494px;top:12px">10:11 / 11:36</span>
  <svg class="abs" style="left:568px;top:10px" width="18" height="16"><rect x="1" y="1" width="16" height="14" rx="3" stroke="#fff" fill="none" stroke-width="1.5"/><rect x="5" y="5" width="8" height="6" fill="#fff"/></svg>
</div>
<h2 class="abs services-title">Our General Services</h2>
<ul class="abs svc-list" style="left:684px"><li>Electrical Installations</li><li>Voice, and Data Cabling</li><li>Electrical Modifications</li><li>Fault Finding</li><li>Panel Upgrades</li><li>Security Lighting</li></ul>
<ul class="abs svc-list" style="left:930px"><li>Generator Hookup</li><li>Surge Protection</li><li>Building Maintenance</li><li>Lift Maintenance</li><li>Crane/Hoist Maintenance</li><li>Labour Hire</li></ul>

<h2 class="abs section-title" style="top:1796px">Testimonials</h2>
<div class="abs portrait" role="img" aria-label="Portrait photo of the client in a suit"></div>
<span class="abs qmark" style="left:414px;top:1862px">“</span>
<p class="abs quote">Lorem Ipsum is simply dummy text of the printing and typesetting industry. Lorem Ipsum has been the industry's standard dummy text ever since the 1500s, when an unknown printer took a galley of type and scrambled it to make a type specimen book...</p>
<span class="abs qmark" style="left:1020px;top:1938px">”</span>
<div class="abs t-name">Marcus Hale</div>
<div class="abs t-role">Business man</div>
<div class="abs t-nav"><i></i><i></i></div>

<footer class="abs site-footer"></footer>
<div class="abs foot-brand"><span class="mark"></span>BRELTON</div>
<div class="abs foot-col" style="left:367px;width:330px">
  <h4>Who We Are?</h4>
  <p>Lorem Ipsum is simply dummy text of the printing and typesetting industry. Lorem Ipsum has been the industry's standard dummy text ever since the 1500s, when an unknown printer took a galley of type and scrambled...</p>
  <span class="more">Read more info ➜</span>
</div>
<div class="abs foot-col" style="left:764px;line-height:28px">
  <h4 style="margin-bottom:10px">Welcome</h4>
  <ul><li>Home</li><li>About Us</li><li>Residential</li><li>Commercial</li><li>Industrial</li><li>Contact Us</li></ul>
</div>
<div class="abs foot-col" style="left:945px;width:200px">
  <h4>Contact Info</h4>
  <p>Ashdale Park, Western Australia, 6190.</p>
  <div class="contact-row" style="margin-top:12px"><svg width="12" height="10" viewBox="0 0 24 18"><rect width="24" height="18" rx="2" fill="#f37122"/></svg>Email: info@brelton.net.au</div>
  <div class="contact-row"><svg width="12" height="12" viewBox="0 0 24 24"><path fill="#f37122" d="M6.6 10.8a15 15 0 0 0 6.6 6.6l2.2-2.2c.3-.3.7-.4 1-.2 1.1.4 2.3.6 3.6.6.6 0 1 .4 1 1V20c0 .6-.4 1-1 1A17 17 0 0 1 3 4c0-.6.4-1 1-1h3.5c.6 0 1 .4 1 1 0 1.3.2 2.5.6 3.6.1.3 0 .7-.2 1z"/></svg>Phone: 0491 372 680</div>
  <div class="contact-row"><svg width="12" height="12" viewBox="0 0 24 24"><rect x="5" y="2" width="14" height="6" fill="#f37122"/><rect x="1" y="9" width="22" height="9" rx="2" fill="#f37122"/><rect x="5" y="15" width="14" height="7" fill="#f37122"/></svg>Fax: 08 6150 24 77</div>
</div>

<div class="abs bottom-bar"></div>
<div class="abs badge"></div>
<div class="abs copyright">© 2016, Brelton. All rights reserved</div>
<div class="abs social">Connct with our social network : <i></i><i></i><i></i><i></i><i></i></div>

</body>
</html>
```